Business card design needed

am looking for a fun and funky design to match our moto, seriously fun swimwear and fashion for girls.

We manufacture and retail girls swimwear and fashion in Australia. Our designs are fun loving and funky. I would like to use bright fuschia to match our website www.berrybloomwear.com.au. We target a higher end market so need it to reflect this.

Industry/Entity Type

Fashion

Contact Information for Business Card

Berry Bloom logo,
Melanie Drew
(07) 39514207
admin@berrybloomwear.com.au
www.berrybloomwear.com.au

Logo Text

Berry Bloom

```html
<!DOCTYPE html>
<html lang="en">
<head>
<meta charset="utf-8">
<title>Berry Bloom – Business Card</title>
<link href="https://fonts.googleapis.com/css2?family=Quicksand:wght@400;500&display=swap" rel="stylesheet">
<style>
  :root {
    --canvas: #3a3c3d;
    --fuchsia: #e0129b;
    --fuchsia-deep: #c80a86;
    --fuchsia-light: #f04cb6;
    --paper: #f7f6f5;
    --petal-yellow: 246, 211, 94;
    --petal-pink: 244, 169, 210;
    --leaf-green: 185, 215, 154;
    --text-light: #fbd8ee;
  }
  * { box-sizing: border-box; margin: 0; padding: 0; }
  html, body {
    width: 1200px;
    height: 900px;
    overflow: hidden;
    background: var(--canvas);
    font-family: "Quicksand", sans-serif;
  }
  .stage {
    width: 1200px;
    height: 900px;
    display: flex;
    flex-direction: column;
    align-items: center;
    justify-content: center;
    gap: 56px;
  }
  .card {
    position: relative;
    width: 640px;
    height: 356px;
    overflow: hidden;
    box-shadow: 0 10px 28px rgba(0, 0, 0, 0.45);
  }

  /* Front */
  .card-front {
    background: linear-gradient(135deg, var(--fuchsia-light) 0%, var(--fuchsia) 45%, var(--fuchsia-deep) 100%);
  }
  .card-front .floral-spray {
    position: absolute;
    right: 0;
    bottom: 0;
    width: 420px;
    height: 340px;
    background:
      radial-gradient(circle 100px at 360px 120px, rgba(var(--petal-pink), 0.8) 0%, rgba(var(--petal-pink), 0) 100%),
      radial-gradient(circle 100px at 150px 270px, rgba(var(--leaf-green), 0.6) 0%, rgba(var(--leaf-green), 0) 100%),
      radial-gradient(circle 170px at 270px 220px, rgba(var(--petal-yellow), 0.9) 0%, rgba(var(--petal-yellow), 0.5) 45%, rgba(var(--petal-yellow), 0) 100%);
  }
  .card-front .brand-name {
    position: absolute;
    left: 48px;
    top: 200px;
    font-size: 42px;
    font-weight: 500;
    color: var(--text-light);
    letter-spacing: 0.5px;
  }

  /* Back */
  .card-back { background: var(--paper); }
  .card-back .floral-wash {
    position: absolute;
    right: 0;
    top: 0;
    width: 380px;
    height: 196px;
    background:
      radial-gradient(ellipse 150px 80px at 150px 80px, rgba(var(--petal-pink), 0.35) 0%, rgba(var(--petal-pink), 0) 100%),
      radial-gradient(ellipse 160px 80px at 250px 120px, rgba(var(--petal-yellow), 0.3) 0%, rgba(var(--petal-yellow), 0) 100%);
  }
  .card-back .brand-name {
    position: absolute;
    left: 40px;
    top: 110px;
    font-size: 42px;
    font-weight: 500;
    color: var(--fuchsia-deep);
    letter-spacing: 0.5px;
  }
  .card-back .contact-band {
    position: absolute;
    left: 0;
    right: 0;
    bottom: 0;
    height: 160px;
    background: linear-gradient(180deg, var(--fuchsia) 0%, var(--fuchsia-deep) 100%);
    display: flex;
    justify-content: space-between;
    align-items: flex-start;
    padding: 44px 36px 0 34px;
    color: var(--text-light);
    font-size: 22px;
    line-height: 1.3;
  }
  .contact-band .person { text-align: left; }
  .contact-band .web { text-align: right; }
</style>
</head>
<body>
  <main class="stage">
    <section class="card card-front">
      <div class="floral-spray" role="img" aria-label="Spray of yellow and pink daisy flowers with green leaves"></div>
      <p class="brand-name">Berry Bloom</p>
    </section>

    <section class="card card-back">
      <div class="floral-wash" role="img" aria-label="Faint pastel daisy flowers"></div>
      <p class="brand-name">Berry Bloom</p>
      <div class="contact-band">
        <div class="person">
          <p class="name">Melanie Drew</p>
          <p class="phone">(07) 39514207</p>
        </div>
        <div class="web">
          <p class="email">admin@berrybloomwear.com.au</p>
          <p class="site">www.berrybloomwear.com.au</p>
        </div>
      </div>
    </section>
  </main>
</body>
</html>
```